Tallant Family Adoption Fundraiser

The sole purpose of this card is to tell people about the fundraiser and direct them to the website that will allow them to participate.  No other contact information is needed.
Since our approach is through personal networking, this card is our sole marketing piece and needs to be effective.  We will use an image of the card for the email & Facebook outreaches we will do.  We have a very limited budget (thus the fundraiser).
We will need a quantity of 2,000 cards.  We dont need to pay for high gloss or metalic finishes, but we were thinking we probably would want a folded business card to give us more real estate to work with.
About the fundraiser (will help you understand the content needed):  Our family is adopting a young girl from Colombia, South America.  We need to raise about $15,000 to bring her home.  This fundraiser is something called a "Duck Race".  People will go to our website and 'purchase' ducks for the race.  For each duck, there will be a rubber duck in the 'race' with their own unique number on it.  On the day of the race, all of the ducks are dumped into a river.  The first ones to cross the finish line down stream is the winner.  The more ducks people put in the race in their name, the more chances they have to win the cash prizes.  We will video the race, and show it on our website.  The idea was to make this an effective and low maintenance fundraiser - nobody has to attend an event - people dont even need to know us, they only need to want to have a chance at the cash prize.  With that being said, here are some ideas of content:
- title:  "The Splendid Paddle Dash"
- "Win 1 of 3 cash prizes totalling $1,000
- www.Welcoming Little Sparrow Back.example
- The Tallant family is adopting a young girl from Colombia, South America, and needs your help to bring her home.
-  We could include a picture of her.
-  We have an icon of a Duck holding a Colombian flag - this is an icon our son created and must be used as the focal point.  We want our existing kids (3 boys) to be part of this and our son Corwin love computer animation and drawing - he created the icon.
-  People can sponsor a duck in the race or simply make their own, individual donation through the website.
-  We are using duck puns like crazy - we will even have a duck pun contest and the winners get free additional ducks in the race.
-  We want our network to be able to use these cards to get others to participate because of the cause - even if they do not know us.  That is why we thought the folded cards would be good because we would have space to put our testimony.  If cost-prohibitive, then we will settle for a 2-sided card.
We are open to suggestions, but time is absolutely of the essence.  We just got approved by Colombia, but we only have 2 weeks left to network with folks in our schools before they are done for the year.  We need a very quick turn-around.

Updates
Due to a browser issue, the icon was not uploaded in my brief.  They are in the process of manually adding it to my brief now and should be available shortly. Thank you for your help.

Target Market(s)
Potential donors/sponsors
Industry/Entity Type
Real Estate
Contact Information for Business Card
www.WelcomingLittleSparrowBack.example
Requirements
Must have
- Catchy but simple exterior to make people want to see the interior of a folded business card.

```html
<!DOCTYPE html>
<html lang="en">
<head>
<meta charset="utf-8">
<title>Tallant Family Adoption Fundraiser Card</title>
<link rel="stylesheet" href="https://fonts.googleapis.com/css2?family=Cabin:wght@400;500&display=swap">
<style>
  :root {
    --page: #eceae6;
    --paper: #ffffff;
    --flag-yellow: #f2e600;
    --flag-blue: #2a3a8f;
    --flag-red: #c8322a;
    --ink-red: #c0392b;
    --ink-dark: #1a1a1a;
  }
  * { box-sizing: border-box; margin: 0; padding: 0; }
  html, body {
    width: 1200px; height: 1000px; overflow: hidden;
    background: var(--page);
    font-family: "Cabin", sans-serif;
    color: var(--ink-red);
  }
  .sheet {
    width: 1200px; height: 1000px;
    display: flex; flex-direction: column;
    align-items: center; justify-content: center; gap: 36px;
  }
  .card {
    width: 780px; height: 446px;
    background: var(--paper);
    padding: 18px;
    box-shadow: 0 2px 8px rgba(0,0,0,0.15);
  }
  .card-frame {
    width: 100%; height: 100%;
    background: var(--paper);
    border: 5px solid var(--flag-red);
    box-shadow: 0 0 0 5px var(--flag-blue), 0 0 0 12px var(--flag-yellow);
    position: relative;
  }

  .mascot-flag {
    background: linear-gradient(135deg, var(--flag-yellow) 0 45%, var(--flag-blue) 45% 68%, var(--flag-red) 68% 100%);
    border-radius: 10px;
  }

  /* Front */
  .card-front .card-frame {
    display: flex; flex-direction: column; align-items: center;
  }
  .card-front .mascot-flag {
    width: 220px; height: 140px; margin-top: 56px;
  }
  .front-url-small {
    font-size: 18px; margin-top: 10px;
  }
  .front-url {
    font-size: 24px; margin-top: auto; margin-bottom: 46px; letter-spacing: 0.2px;
  }

  /* Back */
  .card-back .card-frame {
    display: flex; flex-direction: column; align-items: center;
    padding: 0 30px;
  }
  .card-back .mascot-flag {
    position: absolute; top: 12px; right: 14px;
    width: 120px; height: 76px;
  }
  .race-title {
    font-weight: 400; font-size: 30px; margin-top: 100px;
  }
  .prize-line {
    font-size: 30px; margin-top: 14px;
  }
  .url-badge {
    margin-top: 14px;
    background: var(--flag-yellow);
    border: 2px solid var(--ink-dark);
    box-shadow: 3px 3px 4px rgba(0,0,0,0.45);
    padding: 8px 20px;
    font-size: 22px;
  }
  .cause-text {
    font-size: 23px; line-height: 1.3; text-align: left;
    margin-top: 22px; align-self: flex-start;
  }
</style>
</head>
<body>
<main class="sheet">
  <section class="card card-front">
    <div class="card-frame">
      <div class="mascot-flag" role="img" aria-label="Cartoon duck in sunglasses holding a Colombian flag"></div>
      <p class="front-url-small">www.WelcomingLittleSparrowBack.example</p>
      <p class="front-url">www.WelcomingLittleSparrowBack.example</p>
    </div>
  </section>

  <section class="card card-back">
    <div class="card-frame">
      <div class="mascot-flag" role="img" aria-label="Small cartoon duck holding a Colombian flag"></div>
      <h1 class="race-title">"The Splendid Paddle Dash"</h1>
      <p class="prize-line">"Win 1 of 3 cash prizes totalling $1,000</p>
      <p class="url-badge">www.Welcoming Little Sparrow Back.example</p>
      <p class="cause-text">The Tallant family is adopting a young girl from Colombia,<br>South America, and needs your help to bring her home.</p>
    </div>
  </section>
</main>
</body>
</html>
```